Letterhead for financial advisor-insurance agent firm

Our company, Marlowe Thistle Insurance & Investments, is an insurance (health, life, home, auto, etc) and investment brokerage offering a suite of options to meet client needs. We need letterhead that is professional and embodies strength, security and sophistication.

Industry/Entity Type

Investment

```html
<!DOCTYPE html>
<html lang="en">
<head>
<meta charset="UTF-8">
<title>Marlowe Thistle Letterhead</title>
<link href="https://fonts.googleapis.com/css2?family=Cinzel:wght@400&family=Questrial&display=swap" rel="stylesheet">
<style>
  :root {
    --backdrop: #d6d5d7;
    --paper: #ffffff;
    --navy: #2c2a48;
    --steel: #8ea2ae;
    --name-tint: #a9b7c1;
    --contact-text: #e4e7ee;
    --icon-tint: #a7b5c0;
  }
  * { margin: 0; padding: 0; box-sizing: border-box; }
  html, body {
    width: 900px;
    height: 1200px;
    overflow: hidden;
    background: var(--backdrop);
  }
  .letterhead {
    position: absolute;
    left: 76px;
    top: 45px;
    width: 743px;
    height: 1051px;
    background: var(--paper);
    box-shadow: 0 2px 6px rgba(0,0,0,0.12);
  }
  .header-band {
    position: absolute;
    left: 0; top: 0;
    width: 100%;
    height: 166px;
    background: var(--navy);
    border-bottom: 5px solid var(--steel);
  }
  .brand-square {
    position: absolute;
    left: 22px;
    top: 12px;
    width: 141px;
    height: 140px;
    border: 4px solid var(--steel);
  }
  .company {
    position: absolute;
    right: 15px;
    top: 10px;
    text-align: center;
    font-family: "Cinzel", serif;
    font-weight: 400;
    color: var(--name-tint);
  }
  .company-name {
    display: block;
    font-size: 30px;
    letter-spacing: 1.5px;
    line-height: 1.15;
  }
  .company-tagline {
    display: block;
    font-size: 13px;
    letter-spacing: 1.3px;
    line-height: 1.1;
  }
  .contact-list {
    position: absolute;
    left: 440px;
    top: 65px;
    list-style: none;
    font-family: "Questrial", sans-serif;
    font-size: 17.5px;
    color: var(--contact-text);
  }
  .contact-list li {
    display: flex;
    align-items: center;
    height: 22px;
  }
  .contact-list svg {
    width: 21px;
    height: 19px;
    margin-right: 3px;
    fill: none;
    stroke: var(--icon-tint);
    stroke-width: 2;
  }
  .contact-list svg .solid { fill: var(--icon-tint); stroke: none; }
  .footer-band {
    position: absolute;
    left: 0; bottom: 0;
    width: 100%;
    height: 51px;
    background: var(--navy);
    border-top: 5px solid var(--steel);
  }
</style>
</head>
<body>
  <main class="letterhead">
    <header class="header-band">
      <div class="brand-square" aria-hidden="true"></div>
      <div class="company">
        <span class="company-name">Marlowe Thistle</span>
        <span class="company-tagline">Insurance &amp; Investments</span>
      </div>
      <ul class="contact-list">
        <li>
          <svg viewBox="0 0 24 24" aria-hidden="true"><path class="solid" d="M6.6 10.8a15 15 0 0 0 6.6 6.6l2.2-2.2a1 1 0 0 1 1-.25 11.4 11.4 0 0 0 3.6.57 1 1 0 0 1 1 1V20a1 1 0 0 1-1 1A17 17 0 0 1 3 4a1 1 0 0 1 1-1h3.5a1 1 0 0 1 1 1c0 1.25.2 2.45.57 3.57a1 1 0 0 1-.25 1z"/></svg>
          1472 308 619
        </li>
        <li>
          <svg viewBox="0 0 24 24" aria-hidden="true"><rect x="2.5" y="6" width="19" height="13"/><path d="M2.5 6l9.5 7 9.5-7"/></svg>
          info@marlowethistle.com
        </li>
        <li>
          <svg viewBox="0 0 24 24" aria-hidden="true"><circle cx="12" cy="12" r="9.5"/><ellipse cx="12" cy="12" rx="4" ry="9.5"/><path d="M2.5 12h19M4 7h16M4 17h16"/></svg>
          www.marlowethistle.com
        </li>
        <li>
          <svg viewBox="0 0 24 24" aria-hidden="true"><path class="solid" d="M12 2 1 12h3v10h6v-6h4v6h6V12h3z"/></svg>
          P.O. Box 40827, elm avenue, NY
        </li>
      </ul>
    </header>
    <footer class="footer-band"></footer>
  </main>
</body>
</html>
```